Spring FWC Lawn Care Doorhanger

I need a design for a doorhanger for a lawn care business. The door hanger should focus on the following services: Complete 6 Application Fertilization & Weed Control Program, Spring or Fall Core Aeration and Overseed.
Our business focuses on quality of service.
*Special Offer: Free Grub Control Application *with completion of new 6 app program agreement

I have attached a past version that we have used.

Font styles to use
Serif
Sans Serif

Colors
0054AA
0677BA
7BADD7
CADEEF
E8F1F8
59FF00
82FF00
B8FF75
E3FFCB
F4FFEA

```html
<!DOCTYPE html>
<html lang="en">
<head>
<meta charset="utf-8">
<title>Verdant Turf – Spring Doorhangers</title>
<link href="https://fonts.googleapis.com/css2?family=Montserrat:wght@400;500;600;700;800;900&family=Lobster&display=swap" rel="stylesheet">
<style>
  :root{
    --stage:#333333;
    --blue:#0054AA;
    --blue-mid:#0677BA;
    --blue-pale:#CADEEF;
    --blue-mist:#E8F1F8;
    --green:#5BA327;
    --green-band:#5AA228;
    --green-pale:#E3FFCB;
    --teal:#2A8577;
    --grey-text:#555555;
    --badge-fill:#dfe6dc;
    --white:#ffffff;
  }
  *{box-sizing:border-box;margin:0;padding:0}
  html,body{width:1047px;height:1200px;overflow:hidden;background:var(--stage)}
  body{position:relative;font-family:"Montserrat",Arial,sans-serif}

  .hanger{position:absolute;top:114px;width:390px;height:970px;overflow:hidden;
    background:radial-gradient(ellipse at 50% 55%,#ffffff 55%,#e6e6e6 100%)}
  .hanger--offer{left:108px;border:1px solid #6fb53a}
  .hanger--services{left:553px;border:1px solid var(--blue-mid)}
  .hanger--offer .sky{background:linear-gradient(180deg,#7cc142 0%,#d9eec8 18%,rgba(255,255,255,0) 40%)}
  .hanger--services .sky{background:linear-gradient(180deg,#3b7fc4 0%,#cadeef 18%,rgba(255,255,255,0) 40%)}
  .sky{position:absolute;left:0;top:0;width:100%;height:300px}
  .trim{position:absolute;left:12px;top:10px;right:12px;bottom:10px;border:1px solid #5d9c3a;z-index:6;pointer-events:none}

  .die-cut{position:absolute;left:0;top:0;z-index:2}

  .brand{position:absolute;left:0;top:192px;width:100%;text-align:center;z-index:2}
  .brand__name{font-weight:800;font-size:58px;letter-spacing:1px;color:var(--blue);line-height:1}
  .brand__sub{margin-top:8px;font-weight:700;font-size:15px;color:var(--green);letter-spacing:.2px}

  .photo{position:absolute;left:0;top:290px;width:100%;height:288px;z-index:1}
  .photo--spreader{background:linear-gradient(160deg,#5f7f78 0%,#3f6b5b 35%,#6a9a3a 70%,#7fbf3a 100%)}
  .photo--mower{background:linear-gradient(160deg,#d6a64a 0%,#8a8a55 35%,#5f7d3a 65%,#86c23c 100%)}

  .tag{position:absolute;top:290px;width:111px;height:151px;background:linear-gradient(#ffffff,#f1f1f1);
    border-radius:0 0 55px 55px;z-index:3;text-align:center;box-shadow:0 3px 8px rgba(0,0,0,.25)}
  .tag--award{left:230px}
  .tag--guarantee{left:50px}
  .tag__text{margin-top:10px;font-weight:700;font-size:12px;line-height:16px;color:#444}
  .tag--guarantee .tag__text{color:var(--teal);font-size:13.5px;line-height:18px;margin-top:8px}
  .tag__badge{position:absolute;left:50%;top:54px;width:82px;height:82px;margin-left:-41px;
    border-radius:50%;background:var(--badge-fill)}

  .ribbon{position:absolute;top:528px;height:77px;width:262px;z-index:4;
    transform:skewX(-14deg);border:3px solid var(--white);
    background:linear-gradient(180deg,var(--teal) 0%,#1b6d86 55%,var(--blue) 100%);
    box-shadow:3px 5px 8px rgba(0,0,0,.35)}
  .ribbon--offer{left:60px}
  .ribbon--hello{left:64px}
  .ribbon__text{transform:skewX(14deg);color:var(--white);text-align:center;font-weight:700}
  .ribbon--offer .ribbon__small{font-size:21px;padding-top:4px;line-height:24px}
  .ribbon--offer .ribbon__big{font-size:38px;letter-spacing:9px;line-height:40px}
  .ribbon--hello .ribbon__text{font-size:23px;line-height:30px;padding-top:7px}
  .ribbon-tail{position:absolute;left:49px;top:606px;z-index:3}

  .offer{position:absolute;left:0;top:640px;width:100%;text-align:center;z-index:2}
  .offer__free{font-weight:900;font-size:104px;line-height:96px;color:var(--blue);letter-spacing:-2px}
  .offer__script{font-family:"Lobster",cursive;font-size:40px;color:var(--green);line-height:44px;margin-top:-4px}
  .offer__label{font-weight:600;font-size:13px;color:#444;margin-top:-2px}
  .offer__note{font-weight:400;font-size:9.5px;color:#555;margin-top:6px}

  .intro{position:absolute;left:58px;top:626px;width:300px;font-size:12.5px;line-height:18px;color:var(--grey-text);z-index:2}
  .services{position:absolute;left:45px;top:681px;width:330px;list-style:none;z-index:2}
  .services__item{position:relative;padding-left:103px;font-weight:700;font-size:13px;line-height:21px;color:var(--grey-text)}
  .services__item + .services__item{margin-top:14px}
  .services__dot{position:absolute;left:22px;width:34px;height:34px;border-radius:50%}
  .services__item:first-child .services__dot{top:8px;background:var(--green)}
  .services__item:last-child .services__dot{top:4px;background:var(--blue)}

  .contact{position:absolute;left:0;top:822px;width:100%;height:148px;text-align:center;color:var(--white);z-index:2}
  .hanger--offer .contact{background:var(--green-band)}
  .hanger--services .contact{background:var(--blue)}
  .contact__phone{font-weight:700;font-size:41px;line-height:44px;padding-top:17px}
  .contact__web{font-weight:700;font-size:19px;margin-top:5px}
  .contact__motto{font-weight:700;font-size:10.5px;margin-top:12px}
</style>
</head>
<body>

<!-- Offer side -->
<section class="hanger hanger--offer">
  <div class="sky"></div>
  <svg class="die-cut" width="390" height="300" viewBox="0 0 390 300">
    <line x1="96" y1="11" x2="155" y2="74" stroke="#333" stroke-width="0.8" stroke-dasharray="4 3"/>
    <circle cx="194" cy="114" r="54" fill="none" stroke="#333" stroke-width="0.8" stroke-dasharray="4 3"/>
  </svg>
  <header class="brand">
    <div class="brand__name">VERDANT</div>
    <div class="brand__sub">TURF &amp; OUTDOOR SOLUTIONS</div>
  </header>
  <div class="photo photo--spreader" role="img" aria-label="Lawn spreader applying fertilizer across green grass"></div>
  <div class="tag tag--award">
    <div class="tag__text">FAVOURITE<br>LADSCAPER</div>
    <div class="tag__badge" role="img" aria-label="Award badge"></div>
  </div>
  <div class="ribbon ribbon--offer">
    <div class="ribbon__text">
      <div class="ribbon__small">SPECIAL</div>
      <div class="ribbon__big">OFFER</div>
    </div>
  </div>
  <svg class="ribbon-tail" width="80" height="34" viewBox="0 0 80 34">
    <polygon points="0,0 62,0 80,34" fill="var(--green)"/>
  </svg>
  <div class="offer">
    <div class="offer__free">FREE</div>
    <div class="offer__script">Grub control</div>
    <div class="offer__label">APPLICATION</div>
    <div class="offer__note">*WITH COMPLETION OF NEW 6 APP PROGRAM AGREEMENT</div>
  </div>
  <footer class="contact">
    <div class="contact__phone">(555) 014-2290</div>
    <div class="contact__web">VERDANTTURF.COM</div>
    <div class="contact__motto">OUR BUSINESS FOCUSES ON QUALITY OF SERVICE</div>
  </footer>
  <div class="trim"></div>
</section>

<!-- Services side -->
<section class="hanger hanger--services">
  <div class="sky"></div>
  <svg class="die-cut" width="390" height="300" viewBox="0 0 390 300">
    <line x1="294" y1="11" x2="235" y2="74" stroke="#333" stroke-width="0.8" stroke-dasharray="4 3"/>
    <circle cx="194" cy="114" r="54" fill="none" stroke="#333" stroke-width="0.8" stroke-dasharray="4 3"/>
  </svg>
  <header class="brand">
    <div class="brand__name">VERDANT</div>
    <div class="brand__sub">TURF &amp; OUTDOOR SOLUTIONS</div>
  </header>
  <div class="photo photo--mower" role="img" aria-label="Person pushing a lawn mower across a sunlit lawn"></div>
  <div class="tag tag--guarantee">
    <div class="tag__text">FERTILIZE<br>YOUR LAWN</div>
    <div class="tag__badge" role="img" aria-label="Guarantee badge"></div>
  </div>
  <div class="ribbon ribbon--hello">
    <div class="ribbon__text">WE’RE IN YOUR<br>NEIGHBOURHOOD</div>
  </div>
  <p class="intro">At Verdant Turf and Outdoor Solutions LLC, we’re all about convenience and quality.</p>
  <ul class="services">
    <li class="services__item"><span class="services__dot"></span>COMPLETE 6 APPLICATION<br>FERTILIZATION &amp;<br>WEED CONTROL PROGRAM</li>
    <li class="services__item"><span class="services__dot"></span>SPRING OR FALL CORE<br>AERATION AND OVERSEED</li>
  </ul>
  <footer class="contact">
    <div class="contact__phone">(555) 014-2290</div>
    <div class="contact__web">VERDANTTURF.COM</div>
    <div class="contact__motto">OUR BUSINESS FOCUSES ON QUALITY OF SERVICE</div>
  </footer>
  <div class="trim"></div>
</section>

</body>
</html>
```